KL Taxidermy

I need business Cards with my logo and a background photo of one of my taxidermy mounts.
I would like a black back drop behind it all and what ever looks best for my contact information (red or white?)
Garrick Pembley
592-718-4409
kltaxidermy482@mailnook.example
Chatterloom page

```html
<!DOCTYPE html>
<html lang="en">
<head>
<meta charset="utf-8">
<title>KL Taxidermy – Business Card</title>
<link rel="stylesheet" href="https://fonts.googleapis.com/css2?family=Lato:wght@400;700&family=Oswald:wght@500;600&display=swap">
<style>
  :root {
    --stage: #2b2724;
    --card: #0c0c0c;
    --card-edge: #1c1c1c;
    --ink: #f2f2f2;
    --ink-soft: #d8d8d8;
    --silver: #c9c9c9;
    --divider: #3a3a3a;
  }
  * { margin: 0; padding: 0; box-sizing: border-box; }
  html, body {
    width: 1200px;
    height: 844px;
    overflow: hidden;
    background: var(--stage);
  }
  .stage {
    width: 1200px;
    height: 844px;
    display: flex;
    align-items: center;
    justify-content: center;
    gap: 40px;
  }
  .card {
    position: relative;
    width: 540px;
    height: 310px;
    background: var(--card);
    border: 1px solid var(--card-edge);
    box-shadow: 0 10px 30px rgba(0,0,0,.45);
  }

  /* front side */
  .card-front { display: flex; }
  .brand-panel {
    width: 50%;
    display: flex;
    align-items: center;
    justify-content: center;
    gap: 12px;
    padding-top: 20px;
  }
  .brand-mark {
    width: 14px;
    height: 14px;
    background: var(--ink);
  }
  .brand-name {
    font-family: "Oswald", sans-serif;
    font-weight: 600;
    font-size: 34px;
    letter-spacing: 2px;
    text-transform: uppercase;
    color: var(--ink);
  }
  .contact-panel {
    width: 50%;
    border-left: 1px solid var(--divider);
    margin: 60px 0 60px;
    padding-left: 28px;
    display: flex;
    flex-direction: column;
    justify-content: center;
  }
  .contact-name {
    font-family: "Oswald", sans-serif;
    font-weight: 600;
    font-size: 19px;
    text-transform: uppercase;
    color: var(--ink);
    margin-bottom: 14px;
  }
  .contact-list { list-style: none; }
  .contact-item {
    display: flex;
    align-items: center;
    gap: 8px;
    font-family: "Lato", sans-serif;
    font-size: 13px;
    color: var(--ink-soft);
    line-height: 1.55;
  }
  .contact-item svg { width: 11px; height: 11px; flex: none; fill: var(--ink-soft); }
  .contact-item.social { margin-top: 12px; }
  .social-dot {
    width: 12px; height: 12px; border-radius: 50%;
    background: var(--ink-soft); flex: none;
  }

  /* back side */
  .card-back {
    display: flex;
    align-items: center;
    justify-content: center;
    gap: 14px;
  }
  .card-back .brand-mark { background: var(--silver); width: 16px; height: 16px; }
  .card-back .brand-name { color: var(--silver); font-size: 38px; }
</style>
</head>
<body>
<main class="stage">
  <section class="card card-front" aria-label="Business card, front">
    <div class="brand-panel">
      <span class="brand-mark"></span>
      <span class="brand-name">KL Taxidermy</span>
    </div>
    <div class="contact-panel">
      <h1 class="contact-name">Garrick Pembley</h1>
      <ul class="contact-list">
        <li class="contact-item">
          <svg viewBox="0 0 24 24" aria-hidden="true"><path d="M6.6 10.8a15.1 15.1 0 0 0 6.6 6.6l2.2-2.2a1 1 0 0 1 1-.25 11.4 11.4 0 0 0 3.6.57 1 1 0 0 1 1 1V20a1 1 0 0 1-1 1A17 17 0 0 1 3 4a1 1 0 0 1 1-1h3.5a1 1 0 0 1 1 1c0 1.25.2 2.45.57 3.57a1 1 0 0 1-.25 1z"/></svg>
          592-718-4409
        </li>
        <li class="contact-item">
          <svg viewBox="0 0 24 24" aria-hidden="true"><path d="M2 5h20v14H2z M4 7v.5l8 5 8-5V7l-8 5z" fill-rule="evenodd"/></svg>
          kltaxidermy482@mailnook.example
        </li>
        <li class="contact-item social">
          <span class="social-dot"></span>
          Chatterloom@kltaxidermy
        </li>
      </ul>
    </div>
  </section>

  <section class="card card-back" aria-label="Business card, back">
    <span class="brand-mark"></span>
    <span class="brand-name">KL Taxidermy</span>
  </section>
</main>
</body>
</html>
```